Cedarbrook Residences - Billboard design for our newly renovated townhome community

We have a 5' wide x 4' tall billboard at the entrance to our apartment community, that needs to have the acrylic insert replaced. It is a 2 sided sign, and we are planning to use the same image on both sides. We are called Cedarbrook Residences, and have 48 townhomes that are all 2 bedroom, 1 1/2 bath. A few things we would like to get across on the signage: "Newly Renovated" "2 bed 1 1/2 bath" "Full size W/D in every home" " New Appliances" I've included our parent company's logo - this is the only image I could think of, but it might not be worth having it on the sign. We are in Colorado, so mountain theme could be nice and also sunshine/sun since we are called "Cedarbrook"

Industry/Entity Type

Apartment

Font styles to use
Sans Serif

Requirements
Must have
• Newly Renovated
2 bed 1 1/2 bath
Full size W/D in every home
Virtual Tours available
www.marlowepeaksliving.com
855 - 413 - 9268
Nice to have
• We are located in Colorado - possibly mountain theme? Since our community is called "Cedarbrook Residences" - anything bright with Sun / Sunshine might look really nice as well.

```html
<!DOCTYPE html>
<html lang="en">
<head>
<meta charset="utf-8">
<title>Cedarbrook Residences – Entrance Billboard</title>
<link href="https://fonts.googleapis.com/css2?family=Oswald:wght@400;500;600;700&family=Montserrat:wght@500&display=swap" rel="stylesheet">
<style>
  :root {
    --page: #ececec;
    --white: #ffffff;
    --ink: #111111;
    --red: #e60e0e;
    --band: #1e1e1e;
    --grey-line: #9a9a9a;
    --sky: #dcdcde;
    --roof: #7a4331;
    --wall: #e0a955;
    --ground: #b79d6a;
  }
  * { margin: 0; padding: 0; box-sizing: border-box; }
  html, body {
    width: 800px; height: 1200px; overflow: hidden;
    background: var(--page);
  }
  .billboard {
    position: absolute; left: 20px; top: 296px;
    width: 760px; height: 608px;
    background: var(--white);
    box-shadow: 0 4px 14px rgba(0,0,0,.25);
    overflow: hidden;
  }
  .billboard__shapes { position: absolute; inset: 0; }
  .brand {
    position: absolute; left: 28px; top: 70px;
    display: flex; align-items: center; gap: 10px;
    font-family: "Oswald", sans-serif; font-weight: 500;
    font-size: 22px; color: #3a3a3a; letter-spacing: .5px;
  }
  .brand__mark {
    width: 14px; height: 14px; border-radius: 50%;
    background: var(--red);
  }
  .headline {
    position: absolute; left: 24px; top: 126px;
    font-family: "Oswald", sans-serif; font-weight: 600;
    font-size: 60px; line-height: 70px; letter-spacing: -1px;
    text-transform: uppercase;
  }
  .headline__first { color: var(--ink); display: block; }
  .headline__second { color: var(--red); display: block; }
  .features {
    position: absolute; left: 27px; top: 287px;
    list-style: none;
  }
  .feature {
    display: flex; align-items: center;
    height: 49.5px;
    font-family: "Oswald", sans-serif; font-weight: 500;
    font-size: 19px; color: var(--ink); text-transform: uppercase;
  }
  .feature__icon { width: 40px; height: 40px; margin-right: 18px; flex: none; }
  .call-band {
    position: absolute; left: 0; top: 543px;
    width: 323px; height: 65px;
    background: var(--band); color: var(--white);
    display: flex; align-items: center; gap: 14px;
    padding-left: 24px;
    font-family: "Oswald", sans-serif;
  }
  .call-band__label { font-weight: 700; font-size: 25px; text-transform: uppercase; }
  .call-band__phone { font-weight: 500; font-size: 31px; letter-spacing: -.5px; }
  .web-band {
    position: absolute; left: 505px; top: 569px;
    width: 255px; height: 30px;
    background: var(--band); color: var(--white);
    clip-path: polygon(0 0, 100% 0, 100% 100%, 14px 100%);
    display: flex; align-items: center; gap: 8px;
    padding-left: 22px;
    font-family: "Montserrat", sans-serif; font-weight: 500; font-size: 14px;
  }
</style>
</head>
<body>
<main class="billboard">
  <svg class="billboard__shapes" width="760" height="608" viewBox="0 0 760 608">
    <defs>
      <linearGradient id="houseTones" x1="0" y1="0" x2="0" y2="1">
        <stop offset="0" stop-color="var(--sky)"/>
        <stop offset=".22" stop-color="var(--sky)"/>
        <stop offset=".36" stop-color="var(--roof)"/>
        <stop offset=".55" stop-color="var(--roof)"/>
        <stop offset=".68" stop-color="var(--wall)"/>
        <stop offset=".84" stop-color="#cdb58a"/>
        <stop offset="1" stop-color="var(--ground)"/>
      </linearGradient>
    </defs>
    <polygon class="corner-accent" points="303,0 408,0 381,99" fill="var(--red)"/>
    <polygon class="divider-stripe" points="403,0 412,0 302,608 292,608" fill="var(--red)"/>
    <polygon class="photo" role="img" aria-label="Photo of a two-storey yellow townhome with a brown tiled roof, brick chimneys and a stone garden wall"
      points="413,0 760,0 760,608 304,608" fill="url(#houseTones)"/>
  </svg>

  <div class="brand"><span class="brand__mark"></span>Alderpeak Communities</div>

  <h1 class="headline">
    <span class="headline__first">Cedarbrook</span>
    <span class="headline__second">Residences</span>
  </h1>

  <ul class="features">
    <li class="feature">
      <svg class="feature__icon" viewBox="0 0 40 40" fill="none" stroke="#333" stroke-width="1.4">
        <circle cx="20" cy="20" r="19" stroke="var(--grey-line)" stroke-dasharray="2 2" stroke-width="1"/>
        <path d="M20 1 A19 19 0 0 0 20 39" stroke="var(--red)" stroke-width="2"/>
        <path d="M12 20 L20 13 L28 20 M14 19 V28 H26 V19 M18 28 V23 H22 V28"/>
      </svg>Newly Renovated
    </li>
    <li class="feature">
      <svg class="feature__icon" viewBox="0 0 40 40" fill="none" stroke="#333" stroke-width="1.4">
        <circle cx="20" cy="20" r="19" stroke="var(--grey-line)" stroke-dasharray="2 2" stroke-width="1"/>
        <path d="M20 1 A19 19 0 0 0 20 39" stroke="var(--red)" stroke-width="2"/>
        <path d="M12 17 V12 H17 M12 12 L17 17 M28 17 V12 H23 M28 12 L23 17 M12 23 V28 H17 M12 28 L17 23 M28 23 V28 H23 M28 28 L23 23"/>
      </svg>Full size W/D in every home
    </li>
    <li class="feature">
      <svg class="feature__icon" viewBox="0 0 40 40" fill="none" stroke="#333" stroke-width="1.4">
        <circle cx="20" cy="20" r="19" stroke="var(--grey-line)" stroke-dasharray="2 2" stroke-width="1"/>
        <path d="M20 1 A19 19 0 0 0 20 39" stroke="var(--red)" stroke-width="2"/>
        <rect x="13" y="13" width="14" height="14" rx="3"/>
        <path d="M16.5 20 L19 22.5 L24 17.5"/>
      </svg>Virtual Tours Available
    </li>
    <li class="feature">
      <svg class="feature__icon" viewBox="0 0 40 40" fill="none" stroke="#333" stroke-width="1.4">
        <circle cx="20" cy="20" r="19" stroke="var(--grey-line)" stroke-dasharray="2 2" stroke-width="1"/>
        <path d="M20 1 A19 19 0 0 0 20 39" stroke="var(--red)" stroke-width="2"/>
        <path d="M12 27 V15 H28 V27 M12 22 H28 M15 19 H19 V22 M21 19 H25 V22"/>
      </svg>2 Bed
    </li>
    <li class="feature">
      <svg class="feature__icon" viewBox="0 0 40 40" fill="none" stroke="#333" stroke-width="1.4">
        <circle cx="20" cy="20" r="19" stroke="var(--grey-line)" stroke-dasharray="2 2" stroke-width="1"/>
        <path d="M20 1 A19 19 0 0 0 20 39" stroke="var(--red)" stroke-width="2"/>
        <path d="M11 20 H29 M12 20 V24 A3 3 0 0 0 15 27 H25 A3 3 0 0 0 28 24 V20 M14 27 L13 29 M26 27 L27 29 M14 20 V13 A2 2 0 0 1 18 13"/>
      </svg>1 1/2 Bath
    </li>
  </ul>

  <div class="call-band">
    <span class="call-band__label">Call us</span>
    <span class="call-band__phone">855-413-9268</span>
  </div>

  <div class="web-band">
    <svg width="14" height="14" viewBox="0 0 14 14" fill="none" stroke="#fff" stroke-width="1.1">
      <circle cx="7" cy="7" r="6"/>
      <ellipse cx="7" cy="7" rx="2.6" ry="6"/>
      <path d="M1 7 H13 M2 4 H12 M2 10 H12"/>
    </svg>
    marlowepeaksliving.com
  </div>
</main>
</body>
</html>
```